Business Card Design

redesign of card and recreation of logo based on image provided. the business is located in new york so the Brooklyn Bridge figures prominently in the scheme. product should be very clean.

Industry/Entity Type

Real Estate

Contact Information for Business Card

Wendell Ortwick 318 Tamsin Street Brooklyn, New York 11409 wendell@qorvane.com Mobile: 917-555-0143

Colors
cadf82
1b1b1b
ffffff

Requirements
Nice to have
• Brooklyn Bridge

```html
<!DOCTYPE html>
<html lang="en">
<head>
<meta charset="utf-8">
<title>Ortwick &amp; Assoc — Business Card</title>
<link rel="stylesheet" href="https://fonts.googleapis.com/css2?family=Open+Sans:wght@400;600;700&display=swap">
<style>
  :root {
    --card-black: #1b1b1b;
    --card-deep: #0d0d0d;
    --accent-green: #cadf82;
    --text-white: #ffffff;
    --text-soft: #d9d9d9;
    --rule-grey: #8a8a8a;
    --backdrop: #ebe8e2;
  }
  * { margin: 0; padding: 0; box-sizing: border-box; }
  html, body { width: 1200px; height: 913px; overflow: hidden; }
  body {
    background: var(--backdrop);
    font-family: "Open Sans", Arial, sans-serif;
    position: relative;
  }
  .card {
    position: absolute;
    width: 525px;
    height: 300px;
    border-radius: 16px;
    background: linear-gradient(160deg, #262626 0%, var(--card-black) 45%, var(--card-deep) 100%);
    color: var(--text-white);
    overflow: hidden;
    box-shadow: 0 10px 28px rgba(0,0,0,0.25);
  }
  .card-front { left: 50px; top: 306px; }
  .card-back  { left: 625px; top: 306px; }

  .brand-name {
    position: absolute;
    font-weight: 600;
    color: var(--accent-green);
    letter-spacing: 0.5px;
    white-space: nowrap;
  }
  .card-front .brand-name { right: 34px; top: 62px; font-size: 27px; }
  .card-back .brand-name { left: 0; right: 0; top: 128px; text-align: center; font-size: 38px; }

  .header-rule {
    position: absolute;
    right: 34px; top: 112px;
    width: 280px; height: 1px;
    background: var(--rule-grey);
  }
  .office-address {
    position: absolute;
    right: 34px; top: 128px;
    text-align: right;
    font-size: 13px;
    font-weight: 600;
    line-height: 1.45;
  }

  .tab-stack { position: absolute; left: 0; top: 192px; width: 22px; height: 44px; }
  .tab-stack span { position: absolute; left: 0; width: 22px; height: 14px; background: var(--text-white); }
  .tab-stack span:nth-child(1) { top: 0; background: var(--accent-green); width: 10px; left: 22px; height: 26px; }
  .tab-stack span:nth-child(2) { top: 0; height: 26px; }
  .tab-stack span:nth-child(3) { top: 30px; height: 5px; background: var(--text-soft); }
  .tab-stack span:nth-child(4) { top: 38px; height: 5px; background: var(--text-soft); }

  .agent { position: absolute; left: 42px; top: 186px; }
  .agent-name { font-size: 19px; font-weight: 700; letter-spacing: 0.3px; text-transform: uppercase; }
  .agent-title {
    font-size: 12px; color: var(--accent-green); letter-spacing: 0.5px;
    border-bottom: 1px solid var(--accent-green); display: inline-block; padding-right: 12px;
  }
  .contact-list { list-style: none; position: absolute; left: 42px; top: 234px; font-size: 12.5px; line-height: 15px; }
  .contact-list li { display: flex; align-items: center; gap: 8px; }
  .contact-list svg { width: 10px; height: 10px; fill: none; stroke: var(--accent-green); stroke-width: 1.4; }
</style>
</head>
<body>
  <section class="card card-front" aria-label="Business card front">
    <div class="brand-name">ORTWICK &amp; ASSOC</div>
    <div class="header-rule"></div>
    <address class="office-address" style="font-style:normal">318 Tamsin Street<br>Brooklyn, New York 11409</address>

    <div class="tab-stack" aria-hidden="true"><span></span><span></span><span></span><span></span></div>
    <div class="agent">
      <div class="agent-name">Wendell Ortwick</div>
      <div class="agent-title">BROKER</div>
    </div>
    <ul class="contact-list">
      <li><svg viewBox="0 0 10 10"><path d="M2 1 L4 3 L3 4.5 Q4.5 6.5 5.5 7 L7 6 L9 8 L7.5 9.5 Q2 7 0.5 2.5 Z"/></svg>917-555-0143</li>
      <li><svg viewBox="0 0 10 10"><rect x="2.5" y="0.7" width="5" height="8.6" rx="1"/></svg>917-555-0188</li>
      <li><svg viewBox="0 0 10 10"><rect x="0.7" y="2" width="8.6" height="6"/><path d="M0.7 2 L5 5.5 L9.3 2"/></svg>wendell@qorvane.com</li>
      <li><svg viewBox="0 0 10 10"><circle cx="5" cy="5" r="4.2"/><path d="M0.8 5 H9.2 M5 0.8 Q2.5 5 5 9.2 M5 0.8 Q7.5 5 5 9.2"/></svg>www.qorvane.com</li>
    </ul>
  </section>

  <section class="card card-back" aria-label="Business card back">
    <div class="brand-name">ORTWICK &amp; ASSOC</div>
  </section>
</body>
</html>
```